Commercial Loan Originator Business Card (CHANGE COLORS SCHEME)

CHANGE COLOR SCHEME - SAME DESIGN

Name Miranda Lestock
Title Commercial Loan Originator
Office (800) 641-2905 x68
Direct (240) 731-2264
Email gardenpath4life@mailbox.example

Name Dale Fenwick
Office (800) 641-2905 x70
Direct (410) 392-6058
Email d.fenwickhomes@mailbox.example

Name Gerald Winslow
Office (800) 641-2905 x71
Direct (215) 946-3021
Email g.winslow63@mailbox.example

Name Joan Mallory
Office (800) 641-2905 x
Direct (202) 518-4467
Email jmallory74@mailbox.example

Name Norah Velasco
Office (800) 641-2905 x72
Direct (240) 867-1152
Email capitalhomelending@mailbox.example

```html
<!DOCTYPE html>
<html lang="en">
<head>
<meta charset="utf-8">
<title>Commercial Loan Originator Business Cards</title>
<link rel="stylesheet" href="https://fonts.googleapis.com/css2?family=Tinos:wght@400;700&family=Montserrat:wght@400&display=swap">
<style>
  :root {
    --board: #161616;
    --board-glow: #2a2a2a;
    --accent-grey: #b6b6c0;
    --ink: #ffffff;
    --navy: #0e1328;
    --rust: #b5663a;
    --wine: #521530;
    --orchid: #a83393;
    --slate: #2f3533;
  }
  * { margin: 0; padding: 0; box-sizing: border-box; }
  html, body { width: 1189px; height: 1200px; overflow: hidden; }
  body {
    position: relative;
    background: radial-gradient(ellipse at 50% 40%, var(--board-glow) 0%, var(--board) 70%);
    font-family: "Tinos", "Times New Roman", serif;
    color: var(--ink);
  }
  .card-index {
    position: absolute;
    font-family: "Montserrat", Arial, sans-serif;
    font-size: 24px;
    color: var(--ink);
    line-height: 1;
  }
  .card {
    position: absolute;
    width: 500px;
    height: 286px;
    overflow: hidden;
    box-shadow: 0 6px 16px rgba(0,0,0,0.55);
  }
  .card-art { position: absolute; inset: 0; width: 500px; height: 286px; }
  .card-art .panel { fill: var(--panel); }
  .card-art .arc { fill: var(--accent-grey); }
  .card-art .portrait { fill: var(--photo); }
  .details { position: absolute; left: 307px; top: 75px; right: 6px; }
  .name { font-size: 20px; font-weight: 700; line-height: 1; letter-spacing: 0.2px; white-space: nowrap; }
  .title { font-size: 10.5px; margin-top: 4px; line-height: 1.1; white-space: nowrap; }
  .rule { width: 52px; height: 2px; background: var(--ink); margin-top: 15px; }
  .contacts { list-style: none; margin-top: 36px; font-size: 10.5px; line-height: 15.5px; }
  .contacts li { display: flex; align-items: center; gap: 5px; white-space: nowrap; }
  .contacts svg { width: 8px; height: 8px; fill: var(--ink); flex: none; }

  .card--navy   { --panel: var(--navy);   --photo: #4a5466; left: 73px;  top: 127px; }
  .card--rust   { --panel: var(--rust);   --photo: #6b5448; left: 73px;  top: 458px; }
  .card--wine   { --panel: var(--wine);   --photo: #d9c7c4; left: 73px;  top: 788px; }
  .card--orchid { --panel: var(--orchid); --photo: #8a6e5e; left: 605px; top: 127px; }
  .card--slate  { --panel: var(--slate);  --photo: #8c8f8a; left: 605px; top: 457px; }
</style>
</head>
<body>

<svg width="0" height="0" style="position:absolute">
  <defs>
    <symbol id="icon-phone" viewBox="0 0 10 10"><path d="M1 3.2C1 2 2.2 1.5 5 1.5S9 2 9 3.2V4H7V3.2H3V4H1zM2.5 4.5h5L9 8.5H1z"/></symbol>
    <symbol id="icon-mobile" viewBox="0 0 10 10"><path d="M2 0.5h6v9H2zM3 1.5v7h4v-7z"/></symbol>
    <symbol id="icon-mail" viewBox="0 0 10 10"><path d="M0.5 2h9v6h-9zM1.5 3v4h7V3L5 5.5z"/></symbol>
  </defs>
</svg>

<span class="card-index" style="left:31px; top:250px;">1</span>
<span class="card-index" style="left:31px; top:582px;">2</span>
<span class="card-index" style="left:31px; top:920px;">3</span>
<span class="card-index" style="left:1148px; top:259px;">4</span>
<span class="card-index" style="left:1148px; top:591px;">5</span>

<article class="card card--navy">
  <svg class="card-art" viewBox="0 0 500 286">
    <rect class="panel" width="500" height="286"/>
    <path class="arc" d="M0 0H278C302 70 300 180 212 286H0Z"/>
    <path class="portrait" role="img" aria-label="Portrait photo of the loan originator in a suit in an office" d="M0 0H250C274 70 272 180 188 286H0Z"/>
  </svg>
  <div class="details">
    <div class="name">Gerald Winslow</div>
    <div class="title">Commercial Loan Originator</div>
    <div class="rule"></div>
    <ul class="contacts">
      <li><svg><use href="#icon-phone"/></svg>(800) 641-2905 x71</li>
      <li><svg><use href="#icon-mobile"/></svg>(215) 946-3021</li>
      <li><svg><use href="#icon-mail"/></svg>g.winslow63@mailbox.example</li>
    </ul>
  </div>
</article>

<article class="card card--rust">
  <svg class="card-art" viewBox="0 0 500 286">
    <rect class="panel" width="500" height="286"/>
    <path class="arc" d="M0 0H278C302 70 300 180 212 286H0Z"/>
    <path class="portrait" role="img" aria-label="Portrait photo of the loan originator indoors" d="M0 0H250C274 70 272 180 188 286H0Z"/>
  </svg>
  <div class="details">
    <div class="name">Norah Velasco</div>
    <div class="title">Commercial Loan Originator</div>
    <div class="rule"></div>
    <ul class="contacts">
      <li><svg><use href="#icon-phone"/></svg>(800) 641-2905 x72</li>
      <li><svg><use href="#icon-mobile"/></svg>(240) 867-1152</li>
      <li><svg><use href="#icon-mail"/></svg>capitalhomelending@mailbox.example</li>
    </ul>
  </div>
</article>

<article class="card card--wine">
  <svg class="card-art" viewBox="0 0 500 286">
    <rect class="panel" width="500" height="286"/>
    <path class="arc" d="M0 0H278C302 70 300 180 212 286H0Z"/>
    <path class="portrait" role="img" aria-label="Portrait photo of the loan originator on a light background" d="M0 0H250C274 70 272 180 188 286H0Z"/>
  </svg>
  <div class="details">
    <div class="name">Miranda Lestock</div>
    <div class="title">Commercial Loan Originator</div>
    <div class="rule"></div>
    <ul class="contacts">
      <li><svg><use href="#icon-phone"/></svg>(800) 641-2905 x68</li>
      <li><svg><use href="#icon-mobile"/></svg>(240) 731-2264</li>
      <li><svg><use href="#icon-mail"/></svg>gardenpath4life@mailbox.example</li>
    </ul>
  </div>
</article>

<article class="card card--orchid">
  <svg class="card-art" viewBox="0 0 500 286">
    <rect class="panel" width="500" height="286"/>
    <path class="arc" d="M0 0H278C302 70 300 180 212 286H0Z"/>
    <path class="portrait" role="img" aria-label="Portrait photo of the loan originator outdoors" d="M0 0H250C274 70 272 180 188 286H0Z"/>
  </svg>
  <div class="details">
    <div class="name">Joan Mallory</div>
    <div class="title">Commercial Loan Originator</div>
    <div class="rule"></div>
    <ul class="contacts">
      <li><svg><use href="#icon-phone"/></svg>(800) 641-2905 x</li>
      <li><svg><use href="#icon-mobile"/></svg>(202) 518-4467</li>
      <li><svg><use href="#icon-mail"/></svg>jmallory74@mailbox.example</li>
    </ul>
  </div>
</article>

<article class="card card--slate">
  <svg class="card-art" viewBox="0 0 500 286">
    <rect class="panel" width="500" height="286"/>
    <path class="arc" d="M0 0H278C302 70 300 180 212 286H0Z"/>
    <path class="portrait" role="img" aria-label="Portrait photo of the loan originator in a blazer with a city skyline behind" d="M0 0H250C274 70 272 180 188 286H0Z"/>
  </svg>
  <div class="details">
    <div class="name">Dale Fenwick</div>
    <div class="title">Commercial Loan Originator</div>
    <div class="rule"></div>
    <ul class="contacts">
      <li><svg><use href="#icon-phone"/></svg>(800) 641-2905 x70</li>
      <li><svg><use href="#icon-mobile"/></svg>(410) 392-6058</li>
      <li><svg><use href="#icon-mail"/></svg>d.fenwickhomes@mailbox.example</li>
    </ul>
  </div>
</article>

</body>
</html>
```